Larkfield Pure Website Design

We are working with a water product retailer in Washington called Larkfield Pure.

Some sites to use for content/competitors and inspiration:

https://www.brivolen.com
https://quillmarsh.studio/designs/retail/ (lots of retail website designs we've approved and continue to show clients)

Thank you for taking the time to consider designing a website for us. We are web developers based in Stockton, CA, USA. Most of our projects go through the same process. Understanding this process may help you win a project with us. We custom-code all of our websites in-house. We don’t have any requirements as to what tools you use for your design, but we prefer Figma files. For any design that we label as four-stars, we send it to the client for review. The client picks the final design they want us to use. Once we complete this process, we will continue to show additional clients all the four-star sites and purchase them later. Your designs will have multiple chances to sell. For better chances of success, we ask that you follow these guidelines.

IMAGES:
If you use any images or icons in the design, we ask that you have a link to the asset so we can purchase the image/icon. Most of the designs we submit do not have the customer’s images on them unless they have some great images. Be creative; show us the feeling you are trying to portray with your image choices. Use any royalty-free site you choose. We subscribe to Verimont and mainly use their images, but we can purchase images outside of Verimont.

PLEASE NOTE: we will not submit designs to clients with watermarks on the images.

FONTS:
We ask that you identify the fonts used in the design. This can be done in a message if you want. We typically use Google Fonts and Verimont Fonts.

CONTENT:
We're always open to different content and ideas. We often submit designs with stock images so the client can see our vision. We typically take pictures after the website launch to use their images with our vision. Lorem Ipsum is fine for paragraphs, but we ask that you write the headers in correct English. We want to be able to show the vision and identify the sections of the website.

INSPIRATION:
We typically add a couple of links in the brief of websites we like to help you get started in your design.

REVISIONS:
We do not often ask for revisions of the designs unless we see something in the design that may not appeal to the client. If there are slight changes that we want to make, we do that in the development process.

FEEDBACK:
We rarely give feedback on designs during the design process. We are working on many website projects and do not have the time to provide feedback. We usually respond if your request is well thought out and asks specific questions, but a note asking “feedback, please” usually goes unanswered.

```html
<!DOCTYPE html>
<html lang="en">
<head>
<meta charset="utf-8">
<title>Larkfield Pure</title>
<link href="https://fonts.googleapis.com/css2?family=Montserrat:wght@500;600;700;800&family=Open+Sans:wght@400;600;700&display=swap" rel="stylesheet">
<style>
:root{
  --teal-dark:#0b4a63;
  --teal:#14708f;
  --sky:#4aa6cc;
  --pale:#eaf4f8;
  --pink:#e5186b;
  --ink:#1d2a33;
  --muted:#5c6b74;
  --white:#ffffff;
  --footer:#0c5670;
}
*{box-sizing:border-box;margin:0;padding:0}
html,body{width:1200px;height:4172px;overflow:hidden}
body{position:relative;font-family:'Open Sans',sans-serif;color:var(--ink);background:var(--white)}
.abs{position:absolute}
h1,h2,h3,.nav,.btn{font-family:'Montserrat',sans-serif}

/* hero */
.hero{left:0;top:0;width:1200px;height:960px;overflow:hidden}
.hero-photo{left:0;top:0;width:1200px;height:960px;background:linear-gradient(180deg,#dfeef5 0%,#b9d6e4 22%,#6fa3bd 48%,#3f84a6 70%,#2e7597 100%)}
.hero-product{left:400px;top:230px;width:400px;height:320px;border-radius:24px;background:radial-gradient(ellipse at 50% 45%,#e9f5fb 0%,#a8d1e6 55%,rgba(120,175,205,0) 75%)}
.hero-podium{left:360px;top:500px;width:480px;height:70px;border-radius:50%;background:linear-gradient(180deg,#e8f1f6,#97b9cc)}
.logo{font-family:'Montserrat',sans-serif;font-weight:800;color:var(--white);font-size:26px;display:flex;align-items:center;gap:10px}
.logo .dot{width:14px;height:14px;border-radius:50%;background:var(--sky)}
.header-logo{left:150px;top:22px;color:var(--teal-dark)}
.header-logo{color:var(--teal-dark)}
.nav{left:410px;top:36px;display:flex;gap:22px;font-size:12px;font-weight:700;color:var(--teal-dark)}
.nav .active{color:var(--pink);border-bottom:2px solid var(--pink);padding-bottom:3px}
.btn{display:inline-block;background:var(--pink);color:var(--white);font-weight:700;font-size:12px;border-radius:20px;padding:10px 22px;letter-spacing:.5px}
.nav-cta{left:728px;top:26px}
.call{left:880px;top:22px;display:flex;align-items:center;gap:10px;color:var(--teal-dark)}
.call small{display:block;font-size:9px;font-weight:600}
.call b{font-size:13px}
.hero-title{left:0;top:100px;width:1200px;text-align:center;color:var(--white)}
.hero-title .l1{font-size:48px;font-weight:800;letter-spacing:1px}
.hero-title .l2{font-size:36px;font-weight:800;letter-spacing:1px;margin-top:-4px}
.hero-cta{left:527px;top:562px}

.healthy-title{left:0;top:700px;width:1200px;text-align:center;color:var(--white);font-size:34px;font-weight:800;letter-spacing:1px}
.healthy-title span{font-weight:500}
.benefit{width:220px;height:220px;border-radius:50%;background:var(--white);text-align:center;padding:50px 30px 0;box-shadow:0 10px 30px rgba(10,60,90,.18)}
.benefit h3{font-size:13px;font-weight:800;color:var(--teal-dark);margin:10px 0 6px}
.benefit p{font-size:10px;line-height:1.5;color:var(--muted)}
.benefit.main{background:linear-gradient(180deg,#14708f,#0b4a63);width:270px;height:270px;padding-top:60px}
.benefit.main h3,.benefit.main p{color:var(--white)}
.healthy-fade{left:0;top:900px;width:1200px;height:60px;background:linear-gradient(180deg,rgba(255,255,255,0),#fff)}

/* why choose */
.section-title{left:0;width:1200px;text-align:center;font-size:40px;font-weight:800;color:var(--ink)}
.section-title span{font-weight:500}
.ring{left:0;top:1260px}
.bottle{left:470px;top:1380px;width:260px;height:360px;border-radius:60px 60px 40px 40px;background:linear-gradient(180deg,#cde6f2,#6fb0d0 60%,#2b7da3);}
.feature{width:200px;font-size:11px;line-height:1.6;color:var(--muted)}
.feature h3{font-size:12px;font-weight:800;color:var(--ink);margin-bottom:4px}
.feature.left{text-align:right}
.icon-circle{width:76px;height:76px;border-radius:50%;background:var(--white);border:3px solid var(--teal);display:flex;align-items:center;justify-content:center}
.icon-circle.pink{border-color:var(--pink)}
.icon-circle.filled{background:var(--teal)}

/* products */
.products-bg{left:0;top:2000px;width:1200px;height:720px;background:var(--pale)}
.products-copy{left:260px;top:2140px;width:680px;text-align:center;font-size:12px;line-height:1.6;color:var(--muted)}
.products-cta{left:540px;top:2228px;background:var(--pink)}
.video{left:160px;top:2310px;width:880px;height:380px;border-radius:6px;background:linear-gradient(120deg,#d9dfe3 0%,#f2efe9 40%,#e6d9c8 70%,#bcc7cf 100%)}
.play{left:576px;top:2476px;width:48px;height:48px;border-radius:50%;background:var(--teal);display:flex;align-items:center;justify-content:center}

/* testimonials */
.card{top:2832px;width:380px;height:240px;background:var(--white);border:1px solid #dfe6ea;border-radius:4px;padding:24px 28px;box-shadow:0 6px 20px rgba(0,0,0,.06)}
.card.active{border:2px solid var(--pink)}
.card .who{display:flex;align-items:center;gap:14px;margin-bottom:14px}
.avatar{width:56px;height:56px;border-radius:50%;background:linear-gradient(135deg,#d8c2ad,#9d8470)}
.card .name{font-family:'Montserrat',sans-serif;font-size:13px;font-weight:800}
.stars{color:#f4a21b;font-size:14px;letter-spacing:1px}
.card p{font-size:11.5px;line-height:1.65;color:var(--muted)}

/* scene */
.scene{left:0;top:3100px;width:1200px;height:480px;background:linear-gradient(180deg,#dbe8ee 0%,#a9c3cf 30%,#6b8f8c 55%,#3d7791 75%,#2b6f8c 100%)}
.scene-bottle{left:500px;top:3130px;width:200px;height:360px;border-radius:50px 50px 30px 30px;background:linear-gradient(180deg,#d6ecf6,#7ab8d6 60%,#2f7fa5)}

/* footer */
.footer{left:0;top:3560px;width:1200px;height:612px;background:linear-gradient(180deg,rgba(12,86,112,0) 0%,var(--footer) 14%,#0a465c 100%)}
.footer-logo{left:0;top:3640px;width:1200px;justify-content:center;font-size:40px}
.footer-logo .dot{width:20px;height:20px}
.question{left:300px;top:3795px;color:var(--white);font-family:'Montserrat',sans-serif;font-size:26px;font-weight:700}
.footer-call{left:760px;top:3792px;color:var(--white)}
.col{top:3868px;color:var(--white);font-size:11px;line-height:1.9}
.col h4{font-family:'Montserrat',sans-serif;font-size:12px;font-weight:800;margin-bottom:2px}
.copyright{left:0;top:4132px;width:1200px;text-align:center;color:#cfe4ec;font-size:11px;border-top:1px solid rgba(255,255,255,.2);padding-top:10px}
</style>
</head>
<body>

<!-- hero -->
<section class="abs hero">
  <div class="abs hero-photo" role="img" aria-label="Mountain lake landscape with calm reflective water"></div>
  <div class="abs hero-podium"></div>
  <div class="abs hero-product" role="img" aria-label="Large and small bottles of Larkfield Pure water on a podium"></div>
</section>

<div class="abs logo header-logo"><span class="dot"></span>Larkfield Pure</div>
<nav class="abs nav">
  <span class="active">HOME</span><span>ABOUT US</span><span>SERVICES</span><span>PRODUCTS</span>
</nav>
<span class="abs btn nav-cta">CONTACT US</span>
<div class="abs call">
  <svg width="30" height="30" viewBox="0 0 30 30"><circle cx="15" cy="15" r="14" fill="#fff"/><path d="M11 9l3 3-2 2a8 8 0 0 0 4 4l2-2 3 3-2 2c-5 0-11-6-11-11z" fill="#0b4a63"/></svg>
  <div><small>CALL US TODAY</small><b>+1 (555) 014 2290</b></div>
</div>

<div class="abs hero-title">
  <h1 class="l1">SOURCED FROM NATURE</h1>
  <div class="l2">DELIVERED IN EVERY DROP</div>
</div>
<span class="abs btn hero-cta">GET STARTED ➜</span>

<h2 class="abs healthy-title">HEALTHY LIVING STARTS <span>WITH</span> HEALTHY WATER</h2>
<div class="abs healthy-fade"></div>

<div class="abs benefit" style="left:210px;top:800px">
  <svg width="36" height="36" viewBox="0 0 36 36"><path d="M18 4c6 9 9 13 9 18a9 9 0 0 1-18 0c0-5 3-9 9-18z" fill="none" stroke="#e5186b" stroke-width="2.5"/></svg>
  <h3>SOFTER SKIN &amp; HAIR</h3>
  <p>With exposure to environmental toxins on the rise, filtering your water is essential.</p>
</div>
<div class="abs benefit main" style="left:465px;top:770px">
  <svg width="40" height="40" viewBox="0 0 36 36"><path d="M18 4c6 9 9 13 9 18a9 9 0 0 1-18 0c0-5 3-9 9-18z" fill="none" stroke="#fff" stroke-width="2.5"/></svg>
  <h3>HEALTHIER WATER</h3>
  <p>With exposure to environmental toxins on the rise, filtering your water is essential.</p>
</div>
<div class="abs benefit" style="left:770px;top:800px">
  <svg width="36" height="36" viewBox="0 0 36 36"><circle cx="18" cy="18" r="13" fill="none" stroke="#e5186b" stroke-width="2.5"/><path d="M12 18l4 4 8-8" fill="none" stroke="#e5186b" stroke-width="2.5"/></svg>
  <h3>BETTER TASTE</h3>
  <p>With exposure to environmental toxins on the rise, filtering your water is essential.</p>
</div>

<!-- why choose us -->
<h2 class="abs section-title" style="top:1180px">WHY CHOOSE <span>US</span></h2>
<svg class="abs ring" width="1200" height="640" viewBox="0 1260 1200 640">
  <circle cx="600" cy="1560" r="230" fill="none" stroke="#4aa6cc" stroke-width="3"/>
  <circle cx="475" cy="1365" r="8" fill="#e5186b"/>
  <circle cx="730" cy="1365" r="8" fill="#e5186b"/>
  <line x1="345" y1="1430" x2="380" y2="1430" stroke="#4aa6cc" stroke-width="2"/>
  <line x1="345" y1="1640" x2="380" y2="1640" stroke="#4aa6cc" stroke-width="2"/>
  <line x1="820" y1="1430" x2="855" y2="1430" stroke="#4aa6cc" stroke-width="2"/>
  <line x1="820" y1="1640" x2="855" y2="1640" stroke="#4aa6cc" stroke-width="2"/>
</svg>
<div class="abs bottle" role="img" aria-label="Large Larkfield Pure water jug"></div>

<div class="abs icon-circle" style="left:382px;top:1392px">
  <svg width="34" height="34" viewBox="0 0 34 34"><rect x="7" y="5" width="20" height="24" rx="2" fill="none" stroke="#14708f" stroke-width="2.5"/><path d="M12 12h10M12 17h10M12 22h6" stroke="#14708f" stroke-width="2.5"/></svg>
</div>
<div class="abs icon-circle filled" style="left:382px;top:1602px">
  <svg width="34" height="34" viewBox="0 0 34 34"><circle cx="17" cy="17" r="12" fill="none" stroke="#fff" stroke-width="2.5"/><path d="M11 17l4 4 8-8" fill="none" stroke="#fff" stroke-width="2.5"/></svg>
</div>
<div class="abs icon-circle" style="left:742px;top:1392px">
  <svg width="34" height="34" viewBox="0 0 34 34"><circle cx="17" cy="13" r="6" fill="none" stroke="#14708f" stroke-width="2.5"/><path d="M7 29c1-6 5-9 10-9s9 3 10 9" fill="none" stroke="#14708f" stroke-width="2.5"/></svg>
</div>
<div class="abs icon-circle" style="left:742px;top:1602px">
  <svg width="34" height="34" viewBox="0 0 34 34"><path d="M17 4l11 5v8c0 7-5 11-11 13C11 28 6 24 6 17V9z" fill="none" stroke="#14708f" stroke-width="2.5"/><path d="M12 17l4 4 6-7" fill="none" stroke="#14708f" stroke-width="2.5"/></svg>
</div>
<div class="abs icon-circle pink" style="left:562px;top:1712px">
  <svg width="34" height="34" viewBox="0 0 34 34"><rect x="6" y="8" width="22" height="20" rx="2" fill="none" stroke="#e5186b" stroke-width="2.5"/><path d="M6 14h22M12 5v6M22 5v6" stroke="#e5186b" stroke-width="2.5"/></svg>
</div>

<div class="abs feature left" style="left:140px;top:1396px"><h3>PRODUCT ASSURANCE</h3>Lorem ipsum dolor sit amet, consectetur adipiscing elit, sed do.</div>
<div class="abs feature left" style="left:140px;top:1606px"><h3>SATISFACTION GUARANTEE</h3>Lorem ipsum dolor sit amet, consectetur adipiscing elit, sed do.</div>
<div class="abs feature" style="left:860px;top:1396px"><h3>DEDICATED EXPERTISE</h3>Lorem ipsum dolor sit amet, consectetur adipiscing elit, sed do.</div>
<div class="abs feature" style="left:860px;top:1606px"><h3>TESTED &amp; CERTIFIED</h3>Lorem ipsum dolor sit amet, consectetur adipiscing elit, sed do.</div>
<div class="abs feature" style="left:500px;top:1832px;text-align:center"><h3>DEDICATED EXPERTISE</h3>Lorem ipsum dolor sit amet, consectetur adipiscing elit, sed do.</div>

<!-- products -->
<div class="abs products-bg"></div>
<h2 class="abs section-title" style="top:2064px">OUR <span>PRODUCTS</span></h2>
<p class="abs products-copy">Lorem ipsum dolor sit amet, consectetur adipiscing elit, sed do eiusmod tempor incididunt ut labore et dolore magna aliqua. Ut enim ad minim veniam, quis nostrud exercitation ullamco laboris nisi ut aliquip ex ea commodo consequat. Duis aute irure dolor in reprehenderit in voluptate.</p>
<span class="abs btn products-cta">VIEW MORE ➜</span>
<div class="abs video" role="img" aria-label="Woman drinking a glass of water in a bright kitchen"></div>
<div class="abs play"><svg width="18" height="18" viewBox="0 0 18 18"><path d="M5 3l10 6-10 6z" fill="#fff"/></svg></div>

<!-- testimonials -->
<h2 class="abs section-title" style="top:2748px">OUR <span>TESTIMONIALS</span></h2>

<div class="abs card" style="left:-180px">
  <div class="who"><div class="avatar" role="img" aria-label="Customer portrait"></div><div><div class="name">DANA ELLORY</div><div class="stars">★★★★★</div></div></div>
  <p>Lorem ipsum dolor sit amet, consectetur adipiscing elit, sed do eiusmod tempor incididunt ut labore et dolore magna aliqua. Ut enim ad minim veniam, quis nostrud exercitation ullamco laboris nisi ut aliquip ex ea commodo consequat.</p>
</div>
<div class="abs card" style="left:218px">
  <div class="who"><div class="avatar" role="img" aria-label="Customer portrait"></div><div><div class="name">DANA ELLORY</div><div class="stars">★★★★★</div></div></div>
  <p>Lorem ipsum dolor sit amet, consectetur adipiscing elit, sed do eiusmod tempor incididunt ut labore et dolore magna aliqua. Ut enim ad minim veniam, quis nostrud exercitation ullamco laboris nisi ut aliquip ex ea commodo consequat.</p>
</div>
<div class="abs card active" style="left:612px">
  <div class="who"><div class="avatar" role="img" aria-label="Customer portrait"></div><div><div class="name">DANA ELLORY</div><div class="stars">★★★★★</div></div></div>
  <p>Lorem ipsum dolor sit amet, consectetur adipiscing elit, sed do eiusmod tempor incididunt ut labore et dolore magna aliqua. Ut enim ad minim veniam, quis nostrud exercitation ullamco laboris nisi ut aliquip ex ea commodo consequat.</p>
</div>
<div class="abs card" style="left:1010px">
  <div class="who"><div class="avatar" role="img" aria-label="Customer portrait"></div><div><div class="name">DANA ELLORY</div><div class="stars">★★★★★</div></div></div>
  <p>Lorem ipsum dolor sit amet, consectetur adipiscing elit, sed do eiusmod tempor incididunt ut labore et dolore magna aliqua. Ut enim ad minim veniam, quis nostrud exercitation ullamco laboris nisi ut aliquip ex ea commodo consequat.</p>
</div>

<!-- scene -->
<div class="abs scene" role="img" aria-label="Mountain lake shoreline with rocks and pine trees"></div>
<div class="abs scene-bottle" role="img" aria-label="Larkfield Pure water jug standing at the lake"></div>

<!-- footer -->
<footer class="abs footer"></footer>
<div class="abs logo footer-logo"><span class="dot"></span>Larkfield Pure</div>
<div class="abs question">Have a question? Give us a call.</div>
<div class="abs call footer-call">
  <svg width="30" height="30" viewBox="0 0 30 30"><circle cx="15" cy="15" r="14" fill="#fff"/><path d="M11 9l3 3-2 2a8 8 0 0 0 4 4l2-2 3 3-2 2c-5 0-11-6-11-11z" fill="#0b4a63"/></svg>
  <div><small>CALL US TODAY</small><b>+1 (555) 014 2290</b></div>
</div>

<div class="abs col" style="left:168px">
  <h4>PRODUCTS</h4>
  Whole House Water Filters<br>Whole House Water Softeners<br>Whole House Water Conditioners<br>Under Sink Water Filters<br>Countertop Water Filters<br>Shower Filters<br>Replacement Filters<br>Parts and Accessories
</div>
<div class="abs col" style="left:462px">
  <h4>CUSTOMER SUPPORT</h4>
  Contact Us<br>Check Order Status<br>Shipping, Refunds &amp; Returns<br>Warranty Documents<br>Product Manuals<br>Financing<br>Locate an Installer<br>Installation Videos
</div>
<div class="abs col" style="left:710px">
  <h4>ABOUT</h4>
  Our Story<br>Careers<br>Affiliate Program<br>International Dealers<br>Info Center<br>Certified Products List<br>Patents
</div>
<div class="abs col" style="left:944px">
  <h4>Social Media</h4>
  Pagebook<br>Snapgrid<br>Workline
</div>
<div class="abs copyright">Copyright@2024. All Rights Reserved</div>

</body>
</html>
```